Luxury Resort Complex needs a Power Point Shell

Working in our primary color palate (pms colors can be provided and seen on our web site www.thelumenvale.com) design a title page, chapter page, and three slide page templates that include our logo either screened into the background or somewhere on the page which we can use for internal and external power point presentations.

Target Market(s)

Internal and External constituents

Industry/Entity Type

Hotel

```html
<!DOCTYPE html>
<html lang="en">
<head>
<meta charset="utf-8">
<title>The Lumen Vale — Presentation Templates</title>
<link rel="stylesheet" href="https://fonts.googleapis.com/css2?family=Cormorant+Garamond:wght@400;500&family=Montserrat:wght@400;500;600&display=swap">
<style>
:root{
  --page:#f4f1ec;
  --cream:#efe8de;
  --green:#1f3b31;
  --navy:#1d2c48;
  --coral:#e08878;
  --gold:#b59a6c;
  --ink:#3c3a36;
  --muted:#8d877d;
  --white:#ffffff;
  --serif:"Cormorant Garamond", Georgia, serif;
  --sans:"Montserrat", Arial, sans-serif;
}
*{box-sizing:border-box;margin:0;padding:0}
html,body{width:861px;height:1200px;overflow:hidden;background:var(--page)}
.sheet{
  width:861px;height:1200px;padding:21px 43px;
  display:grid;grid-template-columns:380px 380px;grid-auto-rows:214px;
  column-gap:15px;row-gap:22px;
}
.slide{position:relative;overflow:hidden;background:var(--cream);box-shadow:0 1px 4px rgba(0,0,0,.12);font-family:var(--sans);color:var(--ink)}
.photo{position:absolute}
.side-strip{position:absolute;left:0;top:0;bottom:0;width:22px;border-right:1px solid rgba(181,154,108,.35)}
.side-strip .brand-vertical{position:absolute;left:50%;top:26px;transform:translateX(-50%) rotate(-90deg);transform-origin:center;white-space:nowrap;font-family:var(--serif);font-size:6px;color:var(--gold);letter-spacing:.08em;width:60px;text-align:center}
.side-strip .page-no{position:absolute;bottom:8px;left:0;width:22px;text-align:center;font-size:5px;color:var(--muted)}
.heading{font-family:var(--serif);font-weight:500;line-height:1.05}
.heading.coral{color:var(--coral)}
.heading.light{color:var(--white)}
.body-copy{font-size:5px;line-height:1.55;color:var(--muted)}
.body-copy.light{color:rgba(255,255,255,.75)}
.brand-mark{display:flex;align-items:center;gap:4px;font-family:var(--serif);font-size:7px;color:var(--white);letter-spacing:.05em}
.brand-mark .dot{width:6px;height:6px;border-radius:50%;border:1px solid currentColor}
.crest{width:26px;height:26px;border-radius:50%;border:1px solid var(--gold)}

/* title */
.title-slide .cover{inset:0;background:linear-gradient(180deg,#4f6780 0%,#2c3d50 55%,#1e2b38 100%)}
.title-slide .brand-mark{position:absolute;top:12px;left:50%;transform:translateX(-50%)}
.title-slide .heading{position:absolute;top:80px;width:100%;text-align:center;font-size:20px}
.title-slide .footer{position:absolute;bottom:10px;left:16px;right:16px;display:flex;justify-content:space-between;font-size:5px;color:rgba(255,255,255,.8);letter-spacing:.1em}

/* chapter */
.chapter-slide .cover{inset:0;background:linear-gradient(90deg,rgba(20,28,30,.85) 0%,rgba(40,60,60,.4) 55%,#7aa6b0 100%),linear-gradient(180deg,#c9b79a,#5f8a8c)}
.chapter-slide .heading{position:absolute;left:30px;top:34px;width:190px;font-size:22px}

.presence .columns{position:absolute;left:34px;right:12px;top:44px;bottom:12px;display:grid;grid-template-columns:repeat(5,1fr);gap:4px}
.presence .col{position:relative}
.presence .col span{position:absolute;left:5px;bottom:8px;font-family:var(--serif);font-size:8px;color:var(--white)}

.panel{position:absolute;top:0;bottom:0;display:flex;flex-direction:column;justify-content:center;align-items:center;gap:10px}
.panel.green{background:var(--green)}
.panel.navy{background:var(--navy)}

.contact-list{position:absolute;right:18px;top:18px;list-style:none;display:flex;flex-direction:column;gap:5px}
.contact-list li{display:flex;align-items:center;gap:5px;font-size:5px;color:var(--muted)}
.contact-list svg{width:7px;height:7px;fill:none;stroke:var(--gold);stroke-width:1.4}
</style>
</head>
<body>
<main class="sheet">

  <!-- Title slide -->
  <section class="slide title-slide">
    <div class="photo cover" role="img" aria-label="Resort waterfront and marina at dusk"></div>
    <div class="brand-mark"><span class="dot"></span>The Lumen Vale</div>
    <h1 class="heading light">Where endless possibilities<br>inspire the extraordinary</h1>
    <div class="footer"><span>PRESENTATION TITLE</span><span>www.thelumenvale.com</span></div>
  </section>

  <!-- Text + portrait -->
  <section class="slide">
    <div class="side-strip"><div class="brand-vertical">The Lumen Vale</div><div class="page-no">02</div></div>
    <h2 class="heading coral" style="position:absolute;left:34px;top:18px;width:150px;font-size:17px">Lorem ipsum dolor sit amet</h2>
    <p class="body-copy" style="position:absolute;left:34px;top:62px;width:150px">Consectetur adipiscing elit, sed do eiusmod tempor incididunt ut labore et dolore magna aliqua. Ut enim ad minim veniam, quis nostrud exercitation.</p>
    <div class="photo" style="left:34px;bottom:14px;width:150px;height:72px;background:linear-gradient(135deg,#6f8f6a,#c9b893)" role="img" aria-label="Resort garden terrace with lounge chairs"></div>
    <div class="photo" style="left:200px;top:0;right:0;bottom:0;background:linear-gradient(160deg,#b07b55,#4e3628)" role="img" aria-label="Guest enjoying a drink on the terrace"></div>
  </section>

  <!-- Photo + text -->
  <section class="slide">
    <div class="side-strip"><div class="brand-vertical">The Lumen Vale</div><div class="page-no">03</div></div>
    <div class="photo" style="left:22px;top:0;width:170px;bottom:0;background:linear-gradient(180deg,#dcd5c8,#9fa7a6 60%,#7d8a8f)" role="img" aria-label="Bright suite with balcony over the sea"></div>
    <h2 class="heading coral" style="position:absolute;left:206px;top:62px;width:150px;font-size:17px">Lorem ipsum dolor sit amet</h2>
    <p class="body-copy" style="position:absolute;left:206px;top:106px;width:150px">Sed ut perspiciatis unde omnis iste natus error sit voluptatem accusantium doloremque laudantium, totam rem aperiam.</p>
  </section>

  <!-- Chapter slide -->
  <section class="slide chapter-slide">
    <div class="photo cover" role="img" aria-label="Historic villa courtyard with pool"></div>
    <h2 class="heading light">Surrounded by inspired history and timeless architecture</h2>
  </section>

  <!-- Our Presence -->
  <section class="slide presence">
    <div class="side-strip"><div class="brand-vertical">The Lumen Vale</div><div class="page-no">05</div></div>
    <h2 class="heading coral" style="position:absolute;left:34px;top:16px;font-size:15px">Our Presence</h2>
    <div class="columns">
      <div class="col photo-col" style="background:linear-gradient(180deg,#3a4a6a,#1d2c48)" role="img" aria-label="Resort lobby at night"><span>Resort</span></div>
      <div class="col photo-col" style="background:linear-gradient(180deg,#a7b49a,#5d6e59)" role="img" aria-label="Golf course greens"><span>Golf</span></div>
      <div class="col photo-col" style="background:linear-gradient(180deg,#e5dccd,#b9a98c)" role="img" aria-label="Beach club sand and umbrellas"><span>Beach</span></div>
      <div class="col photo-col" style="background:linear-gradient(180deg,#e9b7a8,#b87a68)" role="img" aria-label="Spa treatment room"><span>Spa</span></div>
      <div class="col photo-col" style="background:linear-gradient(180deg,#d8c7ad,#8f7b5e)" role="img" aria-label="Dining room table setting"><span>Dining</span></div>
    </div>
  </section>

  <!-- About Us -->
  <section class="slide">
    <div class="side-strip"><div class="brand-vertical">The Lumen Vale</div><div class="page-no">06</div></div>
    <div class="photo" style="left:32px;top:12px;width:76px;height:100px;background:linear-gradient(160deg,#5f9a7a,#2e5a48)" role="img" aria-label="Palm trees against the sky"></div>
    <div class="photo" style="left:114px;top:12px;width:96px;height:64px;background:linear-gradient(160deg,#8fc1cc,#4a8a9a)" role="img" aria-label="Pool deck with loungers"></div>
    <div class="photo" style="left:268px;top:96px;width:100px;height:62px;background:linear-gradient(180deg,#e9c6a4,#7f9fb1)" role="img" aria-label="Ocean view at sunset"></div>
    <h2 class="heading coral" style="position:absolute;left:114px;top:96px;font-size:13px">About Us</h2>
    <p class="body-copy" style="position:absolute;left:114px;top:116px;width:140px">Nemo enim ipsam voluptatem quia voluptas sit aspernatur aut odit aut fugit, sed quia consequuntur magni dolores eos qui ratione.</p>
  </section>

  <!-- Bungalows -->
  <section class="slide">
    <div class="panel green" style="left:0;width:150px">
      <div class="crest"></div>
      <h2 class="heading light" style="font-size:22px">Bungalows</h2>
    </div>
    <div class="photo" style="left:150px;top:0;right:0;bottom:0;background:linear-gradient(180deg,#cfe0e6 0%,#e9e4da 55%,#bfb3a0 100%)" role="img" aria-label="Bungalow bedroom opening onto the ocean"></div>
  </section>

  <!-- Make Yourself at Home -->
  <section class="slide">
    <div class="photo" style="left:14px;top:12px;width:180px;height:110px;background:linear-gradient(180deg,#e6ded0,#a99a80)" role="img" aria-label="Arched courtyard of the main building"></div>
    <div class="photo" style="left:14px;top:128px;width:87px;height:74px;background:linear-gradient(160deg,#d9cbb6,#8c7b63)" role="img" aria-label="Guest room interior"></div>
    <div class="photo" style="left:107px;top:128px;width:87px;height:74px;background:linear-gradient(160deg,#b7c7cf,#6e8794)" role="img" aria-label="Bathroom with marble details"></div>
    <div class="panel green" style="left:204px;right:0;align-items:flex-start;justify-content:flex-start;padding:22px 14px">
      <h2 class="heading light" style="font-size:15px">Make Yourself at Home</h2>
      <div style="display:grid;grid-template-columns:1fr 1fr;gap:10px;margin-top:14px">
        <div><h3 class="heading light" style="font-size:8px;margin-bottom:4px">Stay Restful</h3><p class="body-copy light">Quiet rooms, soft linens and calm evenings by the water.</p></div>
        <div><h3 class="heading light" style="font-size:8px;margin-bottom:4px">Neighbors &amp; Friends</h3><p class="body-copy light">Shared gardens and lounges made for easy gatherings.</p></div>
      </div>
    </div>
  </section>

  <!-- Yacht Club -->
  <section class="slide">
    <div class="photo" style="left:0;top:0;width:185px;bottom:0;background:linear-gradient(180deg,#8fb4cf,#3f6a8a 70%,#2b4a63)" role="img" aria-label="Guest relaxing on a yacht deck"></div>
    <div class="panel navy" style="left:185px;right:0">
      <div class="crest"></div>
      <h2 class="heading light" style="font-size:22px">Yacht Club</h2>
    </div>
  </section>

  <!-- Closing / contact -->
  <section class="slide">
    <div class="heading" style="position:absolute;left:34px;top:22px;font-size:18px;color:var(--navy)">The Lumen Vale</div>
    <ul class="contact-list">
      <li><svg viewBox="0 0 10 10"><path d="M2 1h2l1 2.5-1.2 1a5 5 0 0 0 2.7 2.7l1-1.2L10 7v2a1 1 0 0 1-1 1A8 8 0 0 1 0 2a1 1 0 0 1 1-1z"/></svg>+1 (555) 014 2200</li>
      <li><svg viewBox="0 0 10 10"><rect x="1" y="2" width="8" height="6"/><path d="M1 2l4 3.5L9 2"/></svg>info@thelumenvale.com</li>
      <li><svg viewBox="0 0 10 10"><path d="M5 9.5S1.5 6 1.5 4a3.5 3.5 0 0 1 7 0c0 2-3.5 5.5-3.5 5.5z"/><circle cx="5" cy="4" r="1.2"/></svg>www.thelumenvale.com</li>
    </ul>
    <div class="photo" style="left:34px;right:14px;top:72px;bottom:12px;background:linear-gradient(180deg,#a9cbe0 0%,#e8dcc8 50%,#6f8f5e 100%)" role="img" aria-label="Resort facade with palm-lined drive"></div>
  </section>

</main>
</body>
</html>
```